Business Card Re-design

We are looking for a fresh bold look for general office business cards. We are a staffing agency that staffs industrial, coal mining, and clerical jobs.
Tag Line: We connect the RIGHT people with the RIGHT jobs.
Westbrook Office: 2473 W. Tallow Creek Rd, Westbrook, OH - 47308
p. 555.203.6180 f. 555.203.6195
Harlow Office: 264 S. Birch Ln, Harlow, OH - 47152
p. 555.319.2047 f. 555.203.6195
Absentee/Emergency 24hr Hotline 555.203.6172 opt.1
www.bluelanternworkforce.example

```html
<!DOCTYPE html>
<html lang="en">
<head>
<meta charset="utf-8">
<title>Blue Lantern Workforce – Business Cards</title>
<link href="https://fonts.googleapis.com/css2?family=Montserrat:wght@400;500;700;800&display=swap" rel="stylesheet">
<style>
  :root {
    --navy: #1f4a7a;
    --navy-deep: #344a72;
    --sky: #7ab3cc;
    --green: #3f9a45;
    --ink: #3a3f47;
    --paper: #ffffff;
    --backdrop: #ebebeb;
    --font: "Montserrat", sans-serif;
  }
  * { box-sizing: border-box; margin: 0; padding: 0; }
  html, body {
    width: 1200px; height: 1151px; overflow: hidden;
    background: var(--backdrop);
    font-family: var(--font);
  }
  .sheet { position: relative; width: 1200px; height: 1151px; }
  .card {
    position: absolute; left: 160px; width: 880px; height: 503px;
    box-shadow: 0 6px 24px rgba(0,0,0,0.12);
    overflow: hidden;
  }
  .card--back {
    top: 50px;
    background: linear-gradient(135deg, var(--navy-deep) 0%, #4f7899 50%, var(--sky) 100%);
    color: var(--paper);
  }
  .card--front {
    top: 598px;
    background: var(--paper);
    color: var(--ink);
  }

  /* Back */
  .back-brand {
    position: absolute; left: 400px; top: 120px;
    font-weight: 800; font-size: 44px; line-height: 1.05;
    text-transform: uppercase; letter-spacing: 1px; color: var(--paper);
  }
  .tagline {
    position: absolute; left: 120px; top: 300px;
    font-size: 21px; font-weight: 400;
  }
  .tagline strong { font-weight: 800; }
  .back-url {
    position: absolute; left: 120px; top: 350px;
    font-size: 21px; letter-spacing: 0.5px;
  }
  .back-url strong { font-weight: 800; }

  /* Front */
  .front-brand {
    position: absolute; left: 230px; top: 48px;
    display: flex; align-items: center; gap: 16px;
  }
  .front-brand .mark { width: 22px; height: 22px; background: var(--green); flex: none; }
  .front-brand .name {
    font-weight: 800; font-size: 32px; line-height: 1.05;
    text-transform: uppercase; color: var(--navy); letter-spacing: 0.5px;
  }
  .offices {
    position: absolute; left: 56px; top: 200px;
    font-size: 16px; line-height: 1.5;
  }
  .office + .office { margin-top: 14px; }
  .office-name { color: var(--navy); font-weight: 700; }
  .label { color: var(--green); font-weight: 700; }
  .contact-person {
    position: absolute; right: 56px; top: 275px; text-align: right;
  }
  .person-name { color: var(--navy); font-weight: 800; font-size: 27px; }
  .person-title { font-size: 17px; margin-top: 4px; }
  .hotline {
    position: absolute; right: 56px; bottom: 44px; text-align: right;
    font-size: 16px; line-height: 1.35;
  }
  .hotline-title { color: var(--navy); font-weight: 800; font-size: 22px; }
</style>
</head>
<body>
<main class="sheet">

  <section class="card card--back" aria-label="Card back">
    <div class="back-brand">Blue Lantern<br>Workforce</div>
    <p class="tagline">We connect the <strong>RIGHT</strong> people with the <strong>RIGHT</strong> jobs.</p>
    <p class="back-url">www.<strong>bluelanternworkforce</strong>.example</p>
  </section>

  <section class="card card--front" aria-label="Card front">
    <div class="front-brand"><span class="mark"></span><span class="name">Blue Lantern<br>Workforce</span></div>

    <div class="offices">
      <div class="office">
        <div class="office-name">Harlow Office</div>
        <div>264 S. Birch Ln, Harlow, OH-47152</div>
        <div><span class="label">P</span> (555) 319.2047 • <span class="label">F</span> (555) 203.6195</div>
      </div>
      <div class="office">
        <div class="office-name">Westbrook Office</div>
        <div>2473 W. Tallow Creek Rd, Westbrook, OH-47308</div>
        <div><span class="label">P</span> (555) 203.6180 • <span class="label">F</span> (555) 203.6195</div>
      </div>
    </div>

    <div class="contact-person">
      <div class="person-name">Dana WHITFIELD</div>
      <div class="person-title">Managing Director</div>
    </div>

    <div class="hotline">
      <div>Absentee/Emergency</div>
      <div class="hotline-title">24hr Hotline</div>
      <div>555.203.6172 opt.1</div>
    </div>
  </section>

</main>
</body>
</html>
```